Flyer-Design für Zauber-Projekt
Sehr netter und kreativer Kontakt, alle Änderungswünsche wurden kurzfristig umgesetzt, vielen Dank! Meine Flyer gefallen mir super gut! :-)
Zielgruppe
Ich bin Zauberkünstlerin und auf der Suche nach Flyern für ein spezielles Projekt. Dabei handelt es sich um das vermutlich kleinste Zaubertheater der Welt- eine Art Box, die sehr vintage aussieht (wie ein Relikt aus dem 19. Jahrhundert). Wirft man Geld in den Münzschlitz, öffnen sich die Türen des 'Pling-E-Tor' und ich unterhalte das Publikum mit erstaunlichen Zaubereien :-) Zielgruppe sind Firmen, die eine Kunden- und Gäste-Unterhaltung für ihre Messe- oder andere Kundenveranstaltungen (z.B. Tag der offenen Türe, Jubiläen, ...) suchen, oder Kulturschaffende wie Varietès, Theater, Museen etc, in denen der Pling-E-Tor im Wartebereich stehen könnte.
Aufgabenstellung
Der Flyer sollte gerne im 'Vintage-Style' sein, um die 'Magie' des Pling-e-Tor zu transportieren und dennoch ansprechend auf Firmen wirken, d.h. eine Mischung aus Vintage und 'Modern-Professionell' wäre ideal. Weiteres Bildmaterial stelle ich gerne zur Verfügung. Als Schriftart finde ich 'Chopin' oder 'Rochester' sehr schön, vielleicht für die Überschriften?

```html
<!DOCTYPE html>
<html lang="de">
<head>
<meta charset="utf-8">
<title>Pling-E-Tor – Flyer</title>
<link rel="stylesheet" href="https://fonts.googleapis.com/css2?family=Alegreya:wght@400;700&family=Merriweather:wght@300;400;700&display=swap">
<style>
  :root {
    --paper-light: #f2ece2;
    --paper-mid: #e4d9c8;
    --paper-stain: #d6c6ac;
    --paper-edge: #c9b79b;
    --ink: #2b2522;
    --ribbon-red: #b8202c;
    --ribbon-dark: #231f20;
    --ribbon-text: #fbf6ee;
    --rule: #3a3230;
    --frame-dark: #3d1c0c;
    --frame-mid: #7a4420;
    --frame-gold: #c89a4e;
  }
  * { margin: 0; padding: 0; box-sizing: border-box; }
  html, body { width: 864px; height: 1200px; overflow: hidden; }
  body {
    position: relative;
    background:
      radial-gradient(ellipse 260px 180px at 12% 22%, rgba(214,198,172,.45), transparent 70%),
      radial-gradient(ellipse 220px 260px at 28% 78%, rgba(214,198,172,.40), transparent 70%),
      radial-gradient(ellipse 300px 200px at 75% 92%, rgba(201,183,155,.35), transparent 70%),
      radial-gradient(ellipse 180px 140px at 55% 55%, rgba(236,228,214,.6), transparent 70%),
      radial-gradient(ellipse at 40% 45%, var(--paper-light) 0%, var(--paper-mid) 70%, var(--paper-edge) 100%);
    font-family: "Alegreya", Georgia, serif;
    color: var(--ink);
  }
  .hero-photo {
    position: absolute; left: 400px; top: 0; width: 464px; height: 712px;
    background: linear-gradient(90deg,
      rgba(228,217,200,0) 0%, rgba(214,200,180,.7) 14%, #d9d0c2 24%,
      #ebe6de 34%, #f0ece5 55%, #e3dbcf 70%, #c2a673 80%, #8b7a68 88%, #5e5148 100%);
    -webkit-mask-image: linear-gradient(180deg, #000 78%, transparent 100%);
    mask-image: linear-gradient(180deg, #000 78%, transparent 100%);
  }
  .brand {
    position: absolute; left: 45px; top: 50px; width: 410px;
    display: flex; align-items: center; gap: 14px;
    font-family: "Alegreya", Georgia, serif; font-weight: 400;
    font-size: 76px; line-height: 100px; color: #1c1715;
  }
  .brand-mark { width: 12px; height: 12px; background: var(--ribbon-red); flex: none; }
  .rule { position: absolute; height: 1.6px; background: var(--rule); }
  .rule::before, .rule::after {
    content: ""; position: absolute; top: -2.4px; width: 6px; height: 6px;
    border: 1.2px solid var(--rule); border-radius: 50%; background: var(--paper-light);
  }
  .rule::before { left: -6px; } .rule::after { right: -6px; }
  .ribbon {
    position: absolute; display: flex; align-items: center; justify-content: center;
    text-align: center; font-family: "Merriweather", Georgia, serif; font-weight: 300;
    color: var(--ribbon-text);
  }
  .ribbon-red {
    left: 59px; top: 195px; width: 330px; height: 70px; background: var(--ribbon-red);
    font-size: 23px; line-height: 27px;
    clip-path: polygon(0 0, 100% 0, 96.5% 50%, 100% 100%, 0 100%, 3.5% 50%);
  }
  .ribbon-dark {
    left: 56px; width: 316px; height: 28px; background: var(--ribbon-dark); font-size: 14px;
    clip-path: polygon(0 0, 100% 0, 95.5% 50%, 100% 100%, 0 100%, 4.5% 50%);
  }
  .copy { position: absolute; text-align: justify; }
  .intro { left: 45px; top: 283px; width: 345px; font-size: 17.2px; line-height: 22.5px; }
  .body-text { left: 48px; width: 340px; font-size: 13.4px; line-height: 17.4px; }
  .body-text p + p { margin-top: 17.4px; }
  .contact { position: absolute; left: 45px; top: 1098px; width: 340px; text-align: center; font-family: "Merriweather", Georgia, serif; }
  .contact-cta { font-size: 10.5px; line-height: 14px; }
  .contact-mail { font-size: 17px; font-weight: 700; margin-top: 3px; }
  .flourish { position: absolute; left: 123px; top: 1149px; width: 175px; height: 7px; background: #b09670; border-radius: 4px; }
  .frame {
    position: absolute; padding: 12px;
    background: linear-gradient(135deg, var(--frame-dark), var(--frame-mid) 30%, var(--frame-dark) 55%, var(--frame-mid) 80%, var(--frame-dark));
    border: 2px solid #2a1307;
    box-shadow: inset 0 0 0 3px var(--frame-mid), 2px 4px 8px rgba(0,0,0,.4);
  }
  .frame-photo {
    width: 100%; height: 100%;
    border: 2px solid var(--frame-gold);
    box-shadow: 0 0 0 2px #2a1307, inset 0 0 18px rgba(0,0,0,.35);
  }
</style>
</head>
<body>
  <div class="hero-photo" role="img" aria-label="Foto des weiß-goldenen Pling-E-Tor-Kastens mit geschlossenen Türen vor Backsteinwand, daneben Hocker mit Makramee-Bezug"></div>

  <div class="brand"><span class="brand-mark"></span>Pling-E-Tor</div>

  <div class="rule" style="left:48px; top:187px; width:351px;"></div>
  <h1 class="ribbon ribbon-red">Was ist denn bitte ein<br>… Pling-E-Tor?</h1>
  <div class="rule" style="left:48px; top:272px; width:351px;"></div>

  <p class="copy intro">Der Pling-E-Tor ist das wahrscheinlich kleinste Zaubertheater der Welt, in dem Lady Rosalind ihr Publikum in die faszinierende Welt der Magie entführt. Verblüffende Tricks direkt vor den Augen und sogar in den Händen der Zuschauer - ein ganz besonderes Erlebnis, das lange in Erinnerung bleibt!</p>

  <div class="rule" style="left:48px; top:466px; width:331px;"></div>
  <h2 class="ribbon ribbon-dark" style="top:472px;">Der Pling-E-Tor auf Ihrem Event.</h2>
  <div class="rule" style="left:48px; top:504px; width:331px;"></div>

  <div class="copy body-text" style="top:514px;">
    <p>Mieten Sie den Pling-E-Tor für Ihre Messe- oder andere Kundenveranstaltungen, Tag der offenen Tür oder für die Unterhaltung Ihrer Gäste bei großen Hochzeitsfeiern, Jubiläen und anderen Feierlichkeiten. Oder für den Wartebereich von Foyers in Theatern, Museen, Varietès oder anderen Veranstaltungen.</p>
    <p>Der Pling-E-Tor begeistert überall dort, wo Kunden und Gäste warten, flanieren, Sie mit Ihrer Firma Aufmerksamkeit erregen wollen oder Sie Ihren Kunden ein ganz besonderes Erlebnis bieten möchten.</p>
    <p>Mit viel kreativem Herzblut in Eigenregie gestaltet, bereichert der Pling-E-Tor als optischer Blickfang jede Veranstaltung. Die geheimnisvolle Lady Rosalind, die Ihr Publikum mit charmant-humorvoller Zauberei an ihren Sinnen zweifeln lässt, vollendet den Pling-E-Tor zu einem faszinierenden Gesamtkunstwerk.</p>
  </div>

  <div class="rule" style="left:48px; top:843px; width:331px;"></div>
  <h2 class="ribbon ribbon-dark" style="top:849px; font-size:14.5px;">Werbung, die Ihre Kunden verzaubert.</h2>
  <div class="rule" style="left:48px; top:881px; width:331px;"></div>

  <p class="copy body-text" style="left:45px; width:345px; top:891px;">Buchen Sie den Pling-E-Tor für Ihre Messe oder Veranstaltung und stellen Sie eine „magische“ Verbindung zu Ihrer Firma her. Kombinieren Sie den Pling-E-Tor mit Ihren Aufstellern, Beachflags oder Bannern - eine zauberhafte Verknüpfung zwischen Ihrer Firma und dem Kunden-Publikum ist garantiert! Gerne beraten wir Sie über geeignetes Werbematerial.</p>

  <div class="contact">
    <p class="contact-cta">Auf zur Anfrage oder Buchung!</p>
    <p class="contact-mail">petra@zauberwerk-kux.de</p>
  </div>
  <div class="flourish" role="img" aria-label="Zierleiste aus Blattornamenten"></div>

  <div class="frame" style="left:503px; top:447px; width:252px; height:321px;">
    <div class="frame-photo" role="img" aria-label="Foto der Zauberkünstlerin im geöffneten Pling-E-Tor hinter einem roten Samttisch" style="background:linear-gradient(180deg,#e6e1d8 0%,#d8c9a4 18%,#7c7980 34%,#5f5a60 52%,#2e2729 64%,#a71c26 72%,#8f1820 78%,#c6a761 83%,#d9d2c6 100%);"></div>
  </div>
  <div class="frame" style="left:427px; top:801px; width:183px; height:143px;">
    <div class="frame-photo" role="img" aria-label="Foto der Zauberkünstlerin beim Kartentrick mit einem Zuschauer" style="background:linear-gradient(180deg,#7a767c 0%,#5b5559 40%,#2e2628 62%,#a4202a 78%,#7c1a20 100%);"></div>
  </div>
  <div class="frame" style="left:639px; top:815px; width:183px; height:143px;">
    <div class="frame-photo" role="img" aria-label="Foto der Zauberkünstlerin mit Kerze im Inneren des Pling-E-Tor" style="background:linear-gradient(135deg,#858188 0%,#6a656b 40%,#3a3234 70%,#231d1f 100%);"></div>
  </div>
  <div class="frame" style="left:522px; top:978px; width:204px; height:159px;">
    <div class="frame-photo" role="img" aria-label="Foto einer Hand, die eine Münze in den Münzschlitz wirft" style="background:linear-gradient(90deg,#e8e4de 0%,#dedad3 55%,#cdb27a 80%,#b8955a 100%);"></div>
  </div>
</body>
</html>
```